A start-up named "Corvath Therapeutics" - needs a new PowerPoint design

We need a new PowerPoint Design for an early-stage start-up named "Corvath Therapeutics" seeking to disrupt the current approach towards drug discovery within aging disorders.

We would like to build on Corvath's legacy, the founder of the modern science of genetics, by employing a multidisciplinary approach, experimenting, and providing elderly patients the attention they deserve.

We have selected the suffix "therapeutics" intentionally as it stands for (a medicine) the treatment of disease; the science of healing. Alzheimer’s treatment is a huge, urgent, unmet need:
- Shift from a disease-management system to a preventive medicine system
- Focus on increasing the health span, not only the life span

Target Market(s)

Pharma/ Biotech Executives Medical Institutions Healthcare professionals (MDs, nurses, payors, pharmacists, etc.) Patients

Industry/Entity Type

Healthcare

Other font styles liked:
• Celias

Colors
0054AA
0677BA
7BADD7
CADEEF
E8F1F8
E54698
E96AAD
F1A4CE
F9D9EA
FCEFF6
A7469A
B969AE
D3A5CF
EDDBEB
F8F0F9
6B429C
8869AF
B7A5CE
E3DAEB
F3F0F8

Requirements
Must have
• - differentiate from other companies named after Corvath - differentiate from other Pharma/ Biotech companies
Nice to have
• simplicity/ minimalist logo vivid colors gradient 3D Life-Sciences inspired Simple geometry Balance
Should not have
• mascot/ emblem watermark logo animated ink style nature-inspired inventive typography artistic chaos

```html
<!DOCTYPE html>
<html lang="en">
<head>
<meta charset="utf-8">
<title>Corvath Therapeutics – Presentation Template</title>
<link href="https://fonts.googleapis.com/css2?family=Poppins:wght@400;500;600;700&display=swap" rel="stylesheet">
<style>
:root{
  --plum:#6a0a43;
  --magenta:#a3116c;
  --berry:#8a0c5a;
  --orange:#f3a21a;
  --orange-dark:#d98a10;
  --ink:#1e1e1e;
  --grey:#6f6f6f;
  --line:#e6e6e6;
  --canvas:#dcdcdc;
}
*{box-sizing:border-box;margin:0;padding:0}
html,body{width:785px;height:1200px;overflow:hidden;background:var(--canvas);font-family:'Poppins',sans-serif;color:var(--ink)}
.deck{display:grid;grid-template-columns:repeat(3,252px);column-gap:7.5px;row-gap:7px;padding:7px}
.slide{position:relative;width:252px;height:142px;background:#fff;overflow:hidden}
.abs{position:absolute}
/* covers */
.cover{display:flex;flex-direction:column;align-items:center;color:#fff;text-align:center}
.cover .bg{position:absolute;inset:0}
.brand{position:relative;display:flex;align-items:center;gap:3px;font-weight:600;font-size:8px;margin-top:30px;color:#fff}
.brand .mark{width:9px;height:9px;background:currentColor;opacity:.9}
.cover h1{position:relative;font-size:15.5px;line-height:15px;font-weight:700;margin-top:6px}
.cover .sub{position:relative;font-size:5.6px;margin-top:2px}
.pill{position:absolute;left:95px;top:115px;width:54px;height:9px;border-radius:5px;font-size:3.4px;font-weight:600;display:flex;align-items:center;justify-content:center;color:#fff;background:var(--plum)}
.pill.gold{background:var(--orange)}
/* content */
.title{position:absolute;left:14px;top:18px;font-size:11px;font-weight:600;color:var(--ink)}
.title::after{content:"";display:block;width:11px;height:2px;background:var(--orange);margin-top:2px}
.title.center{left:0;right:0;text-align:center}
.title.center::after{margin:2px auto 0}
.body{font-size:3.2px;line-height:4.3px;color:var(--grey)}
.pname{font-size:3.8px;font-weight:600;color:var(--magenta);line-height:5px}
.footer{position:absolute;left:0;right:0;bottom:6px;height:5px}
.footer .fname{position:absolute;left:3px;top:0;font-size:3.4px;font-weight:600;color:var(--plum);display:flex;align-items:center;gap:1px}
.footer .fname i{display:block;width:4px;height:4px;background:var(--plum)}
.footer .bar{position:absolute;left:26px;right:22px;top:1px;height:3.5px;background:linear-gradient(90deg,var(--plum),var(--magenta));transform:skewX(-30deg);color:#fff;font-size:2.2px;text-align:center;line-height:3.5px;letter-spacing:.2px}
.footer .num{position:absolute;right:5px;top:1px;width:14px;height:3.5px;background:var(--orange);transform:skewX(-30deg);font-size:2.2px;color:#fff;text-align:center;line-height:3.5px}
.icon-sq{width:9px;height:9px;border:1.2px solid var(--magenta)}
.icon-ring{width:12px;height:12px;border-radius:50%;background:#fff;box-shadow:0 0 2px rgba(0,0,0,.25);display:flex;align-items:center;justify-content:center}
.icon-ring::after{content:"";width:5px;height:5px;border-radius:50%;border:1px solid var(--magenta)}
.item{position:absolute;display:flex;gap:4px;width:108px}
.stat{position:absolute;width:60px;text-align:center}
.stat b{display:block;font-size:10px;color:var(--orange);font-weight:600}
table.data{border-collapse:collapse;width:206px;font-size:3.2px}
table.data th{background:var(--plum);color:#fff;height:11px;font-weight:600}
table.data td{height:11.7px;text-align:center;color:var(--grey);border-bottom:.4px solid var(--line)}
table.data td.key{background:var(--orange);color:#fff;font-weight:600}
table.data tr:nth-child(odd) td:not(.key){background:#f4f4f4}
.card{position:absolute;top:58px;width:57px;height:54px;border-radius:3px;color:#fff;text-align:center;padding:18px 5px 0}
.card .pname{color:#fff}
.card .body{color:rgba(255,255,255,.85)}
.card .icon-ring{position:absolute;left:22px;top:-6px;width:14px;height:14px}
.contact{position:absolute;left:34px;width:67px;height:15px;background:#fff;box-shadow:0 0 2px rgba(0,0,0,.15);display:flex;align-items:center;gap:6px;padding-left:6px;font-size:2.8px;color:var(--grey)}
.contact.top{background:var(--plum);color:#fff}
.contact svg{flex:none}
</style>
</head>
<body>
<main class="deck">

<!-- 1 -->
<section class="slide cover">
  <div class="bg" role="img" aria-label="Dark photo of two hands reaching toward each other" style="background:linear-gradient(90deg,#2b2b2b,#4e4e4e 50%,#2d2d2d)"></div>
  <div class="brand"><span class="mark"></span>Corvath Therapeutics</div>
  <h1>Presentation<br>Title Goes Here</h1>
  <p class="sub">Sub Title Goes Here</p>
  <div class="pill">Oct 2021</div>
</section>

<!-- 2 -->
<section class="slide cover" style="background:#000">
  <div class="brand" style="margin-top:24px;font-size:5.5px;color:var(--magenta)"><span class="mark" style="width:6px;height:6px"></span>Corvath Therapeutics</div>
  <h1 style="margin-top:4px">Presentation<br>Title Goes Here</h1>
  <p class="sub">Sub Title Goes Here</p>
  <div class="pill" style="top:108px">Oct 2021</div>
</section>

<!-- 3 -->
<section class="slide cover">
  <div class="bg" role="img" aria-label="Magenta-toned photo of two hands reaching toward each other" style="background:linear-gradient(90deg,#7a1a58,#c2468f 50%,#9c1a6c)"></div>
  <div class="brand"><span class="mark"></span>Corvath Therapeutics</div>
  <h1>Presentation<br>Title Goes Here</h1>
  <p class="sub">Sub Title Goes Here</p>
  <div class="pill gold">Jan 2022</div>
</section>

<!-- 4 -->
<section class="slide cover">
  <div class="bg" role="img" aria-label="Purple background with a faint molecular network pattern" style="background:radial-gradient(circle at 50% 40%,#a4156e,#6a0a43 85%)"></div>
  <div class="brand"><span class="mark"></span>Corvath Therapeutics</div>
  <h1>Presentation<br>Title Goes Here</h1>
  <p class="sub">Sub Title Goes Here</p>
  <div class="pill gold">Oct 2021</div>
</section>

<!-- 5 -->
<section class="slide cover" style="color:var(--ink)">
  <div class="brand" style="color:var(--magenta);margin-top:30px"><span class="mark"></span>Corvath Therapeutics</div>
  <h1>Presentation<br>Title Goes Here</h1>
  <p class="sub">Sub Title Goes Here</p>
  <div class="pill" style="left:98px">Oct 2021</div>
</section>

<!-- 6 -->
<section class="slide">
  <h2 class="title">Title And Body Slide</h2>
  <div class="footer"><span class="fname"><i></i>Corvath</span><div class="bar">CORVATH | Copyright ©</div><div class="num">6</div></div>
</section>

<!-- 7 -->
<section class="slide">
  <h2 class="title" style="top:20px">Title And Body Slide</h2>
  <div class="abs body" style="left:14px;top:46px;width:224px">
    <p>Lorem ipsum dolor sit amet, consectetur adipiscing elit, sed do eiusmod tempor incididunt ut labore et dolore magna aliqua. Lorem ipsum dolor sit amet, consectetur adipiscing elit, sed do eiusmod tempor incididunt ut labore et dolore magna aliqua. Ut enim ad minim veniam, quis nostrud exercitation ullamco laboris nisi ut aliquip.</p>
    <p style="margin-top:3px">Lorem ipsum dolor sit amet, consectetur adipiscing elit. Lorem ipsum dolor sit amet, consectetur adipiscing elit, sed do eiusmod tempor incididunt ut labore et dolore magna aliqua. Lorem ipsum dolor sit amet, consectetur adipiscing elit, sed do eiusmod tempor incididunt ut labore et dolore magna aliqua. Ut enim ad minim veniam.</p>
    <p style="margin-top:3px">Lorem ipsum dolor sit amet, consectetur adipiscing elit, sed do eiusmod tempor incididunt ut labore et dolore magna aliqua. Lorem ipsum dolor sit amet, consectetur adipiscing elit, sed do eiusmod tempor incididunt ut labore et dolore magna aliqua. Lorem ipsum dolor sit amet, consectetur adipiscing elit, sed do eiusmod tempor incididunt ut labore et dolore magna aliqua. Lorem ipsum dolor sit amet, sed do eiusmod tempor incididunt ut labore et dolore magna aliqua. Ut enim ad minim veniam, quis nostrud exercitation ullamco laboris nisi ut aliquip.</p>
  </div>
  <div class="footer"><span class="fname"><i></i>Corvath</span><div class="bar">CORVATH | Copyright ©</div><div class="num">7</div></div>
</section>

<!-- 8 -->
<section class="slide">
  <h2 class="title" style="top:20px">Title And Body Slide</h2>
  <p class="abs" style="left:15px;top:49px;font-size:6px;font-weight:600;color:var(--plum)">Here Add Your Title</p>
  <div class="abs body" style="left:15px;top:62px;width:68px">• Lorem ipsum dolor sit amet, consectetur adipiscing elit, sed do eiusmod tempor incididunt ut labore et dolore magna aliqua.<br><br>• Ut enim ad minim veniam, quis nostrud exercitation ullamco laboris nisi ut aliquip ex.<br><br>• Lorem ipsum dolor sit amet, consectetur adipiscing elit, sed do eiusmod tempor incididunt.</div>
  <div class="abs body" style="left:90px;top:62px;width:68px">• Lorem ipsum dolor sit amet, consectetur adipiscing elit, sed do eiusmod tempor incididunt ut labore et dolore magna aliqua.<br><br>• Ut enim ad minim veniam, quis nostrud exercitation ullamco laboris nisi ut aliquip ex.<br><br>• Lorem ipsum dolor sit amet, consectetur adipiscing elit, sed do eiusmod tempor incididunt.</div>
  <div class="abs body" style="left:166px;top:62px;width:68px">• Lorem ipsum dolor sit amet, consectetur adipiscing elit, sed do eiusmod tempor incididunt ut labore et dolore magna aliqua.<br><br>• Ut enim ad minim veniam, quis nostrud exercitation ullamco laboris nisi ut aliquip ex.<br><br>• Lorem ipsum dolor sit amet, consectetur adipiscing elit, sed do eiusmod tempor incididunt.</div>
  <div class="footer"><span class="fname"><i></i>Corvath</span><div class="bar">CORVATH | Copyright ©</div><div class="num">8</div></div>
</section>

<!-- 9 -->
<section class="slide">
  <div class="abs" style="left:25px;top:36px;width:110px;height:60px;background:var(--magenta)"></div>
  <div class="abs" role="img" aria-label="Photo of hands typing on a laptop" style="left:0;top:20px;width:122px;height:68px;background:linear-gradient(120deg,#cfc7bd,#8a6a4a 55%,#3a2e28)"></div>
  <h2 class="title" style="left:147px;top:38px">Pic And Text</h2>
  <p class="abs body" style="left:147px;top:64px;width:88px">Lorem ipsum dolor sit amet, consectetur adipiscing elit, sed do eiusmod tempor incididunt ut labore et dolore magna aliqua. Lorem ipsum dolor sit amet, consectetur adipiscing elit, sed do eiusmod tempor incididunt ut labore et dolore magna aliqua. Ut enim ad minim veniam, quis nostrud exercitation ullamco laboris nisi ut aliquip.</p>
  <div class="footer"><span class="fname"><i></i>Corvath</span><div class="bar">CORVATH | Copyright ©</div><div class="num">9</div></div>
</section>

<!-- 10 -->
<section class="slide">
  <h2 class="title" style="top:8px">Title And Body Slide</h2>
  <div class="item" style="left:14px;top:42px"><div class="icon-sq"></div><div><p class="pname">Project name</p><p class="body">Lorem ipsum dolor sit amet, nec an dictas equidem appellantur, ut has commune accommodare.</p></div></div>
  <div class="item" style="left:128px;top:42px"><div class="icon-sq"></div><div><p class="pname">Project name</p><p class="body">Lorem ipsum dolor sit amet, nec an dictas equidem appellantur, ut has commune accommodare.</p></div></div>
  <div class="item" style="left:14px;top:69px"><div class="icon-sq"></div><div><p class="pname">Project name</p><p class="body">Lorem ipsum dolor sit amet, nec an dictas equidem appellantur, ut has commune accommodare.</p></div></div>
  <div class="item" style="left:128px;top:69px"><div class="icon-sq"></div><div><p class="pname">Project name</p><p class="body">Lorem ipsum dolor sit amet, nec an dictas equidem appellantur, ut has commune accommodare.</p></div></div>
  <div class="item" style="left:14px;top:96px"><div class="icon-sq"></div><div><p class="pname">Project name</p><p class="body">Lorem ipsum dolor sit amet, nec an dictas equidem appellantur, ut has commune accommodare.</p></div></div>
  <div class="item" style="left:128px;top:96px"><div class="icon-sq"></div><div><p class="pname">Project name</p><p class="body">Lorem ipsum dolor sit amet, nec an dictas equidem appellantur, ut has commune accommodare.</p></div></div>
  <div class="footer"><span class="fname"><i></i>Corvath</span><div class="bar">CORVATH | Copyright ©</div><div class="num">10</div></div>
</section>

<!-- 11 -->
<section class="slide">
  <h2 class="title center" style="top:10px">6 Columns Slide</h2>
  <div class="item" style="left:20px;top:42px;width:100px"><div class="icon-ring"></div><div><p class="pname">Project name</p><p class="body">Lorem ipsum dolor sit amet, nec an dictas equidem appellantur, ut has commune accommodare.</p></div></div>
  <div class="item" style="left:134px;top:42px;width:100px"><div class="icon-ring"></div><div><p class="pname">Project name</p><p class="body">Lorem ipsum dolor sit amet, nec an dictas equidem appellantur, ut has commune accommodare.</p></div></div>
  <div class="item" style="left:20px;top:68px;width:100px"><div class="icon-ring"></div><div><p class="pname">Project name</p><p class="body">Lorem ipsum dolor sit amet, nec an dictas equidem appellantur, ut has commune accommodare.</p></div></div>
  <div class="item" style="left:134px;top:68px;width:100px"><div class="icon-ring"></div><div><p class="pname">Project name</p><p class="body">Lorem ipsum dolor sit amet, nec an dictas equidem appellantur, ut has commune accommodare.</p></div></div>
  <div class="item" style="left:20px;top:96px;width:100px"><div class="icon-ring"></div><div><p class="pname">Project name</p><p class="body">Lorem ipsum dolor sit amet, nec an dictas equidem appellantur, ut has commune accommodare.</p></div></div>
  <div class="item" style="left:134px;top:96px;width:100px"><div class="icon-ring"></div><div><p class="pname">Project name</p><p class="body">Lorem ipsum dolor sit amet, nec an dictas equidem appellantur, ut has commune accommodare.</p></div></div>
  <div class="footer"><span class="fname"><i></i>Corvath</span><div class="bar">CORVATH | Copyright ©</div><div class="num">11</div></div>
</section>

<!-- 12 -->
<section class="slide">
  <h2 class="title center" style="top:16px">Here Goes Title Of This Slide</h2>
  <p class="abs body" style="left:28px;top:49px;width:196px;text-align:center">Lorem Ipsum the printing and typesetting industry. Lorem Ipsum has been the industry's standard dummy text ever since the 1500s, when an unknown printer took a galley of type and scrambled it to make a type specimen book. It has survived not only five centuries.</p>
  <div class="stat body" style="left:22px;top:79px"><b>1M</b>Lorem Ipsum has been the industry's standard dummy text ever since the 1500s</div>
  <div class="stat body" style="left:96px;top:79px"><b>2022</b>Lorem Ipsum has been the industry's standard dummy text ever since</div>
  <div class="stat body" style="left:168px;top:79px"><b>150+</b>Lorem Ipsum has been the industry's standard dummy text ever since the 1500s</div>
  <div class="footer"><span class="fname"><i></i>Corvath</span><div class="bar">CORVATH | Copyright ©</div><div class="num">12</div></div>
</section>

<!-- 13 -->
<section class="slide">
  <div class="abs" style="left:16px;top:12px;width:108px;height:53px;border-radius:2px;background:linear-gradient(135deg,var(--orange),var(--orange-dark));padding:9px 7px;color:#fff">
    <p style="font-size:5.5px;font-weight:500">Text Here</p>
    <p class="body" style="color:rgba(255,255,255,.85);margin-top:4px">Lorem ipsum dolor sit amet, consectetur adipiscing elit, sed do eiusmod tempor incididunt ut labore et dolore magna aliqua. Ut enim ad minim veniam, quis nostrud exercitation ullamco laboris nisi ut aliquip ex.</p>
  </div>
  <p class="abs body" style="left:132px;top:29px;width:98px">Lorem ipsum dolor sit amet, consectetur adipiscing elit, sed do eiusmod tempor incididunt ut labore et dolore magna aliqua. Ut enim ad minim veniam, quis nostrud exercitation ullamco laboris nisi ut aliquip ex.</p>
  <p class="abs" style="left:24px;top:82px;width:100px;font-size:8.5px;line-height:11px;font-weight:600">Lorem ipsum dolor sit amet consect adipiscing elit</p>
  <div class="abs" style="left:130px;top:68px;width:107px;height:54px;border-radius:2px;background:linear-gradient(135deg,var(--plum),var(--magenta));padding:9px 7px;color:#fff">
    <p style="font-size:5.5px;font-weight:500">Text Here</p>
    <p class="body" style="color:rgba(255,255,255,.85);margin-top:4px">Lorem ipsum dolor sit amet, consectetur adipiscing elit, sed do eiusmod tempor incididunt ut labore et dolore magna aliqua. Ut enim ad minim veniam, quis nostrud exercitation ullamco laboris nisi ut aliquip ex.</p>
  </div>
  <div class="footer"><span class="fname"><i></i>Corvath</span><div class="bar">CORVATH | Copyright ©</div><div class="num">13</div></div>
</section>

<!-- 14 -->
<section class="slide">
  <div class="abs" style="left:0;top:0;width:252px;height:72px;background:linear-gradient(90deg,var(--plum),var(--magenta))"></div>
  <h2 class="abs" style="left:0;right:0;top:14px;text-align:center;color:#fff;font-size:11px;font-weight:600">Here Add Awesome Text</h2>
  <p class="abs body" style="left:36px;top:40px;width:180px;text-align:center;color:rgba(255,255,255,.8)">Lorem ipsum dolor sit amet, consectetur adipiscing elit, sed do eiusmod tempor incididunt ut labore et dolore magna aliqua. Lorem ipsum dolor sit amet, consectetur adipiscing elit.</p>
  <svg class="abs" style="left:0;top:0" width="252" height="142" aria-hidden="true">
    <g fill="var(--orange)" stroke="#fff" stroke-width="1.2"><circle cx="51" cy="71" r="11"/><circle cx="124" cy="71" r="11"/><circle cx="197" cy="71" r="11"/></g>
    <g fill="none" stroke="#fff" stroke-width=".8"><circle cx="51" cy="71" r="4"/><circle cx="124" cy="71" r="4"/><circle cx="197" cy="71" r="4"/></g>
  </svg>
  <div class="abs body" style="left:20px;top:88px;width:62px;text-align:center"><p class="pname">Project name</p>Lorem ipsum dolor sit amet, nec an dictas equidem appellantur, ut has commune accommodare. Mea illum, ludus solet idpro.</div>
  <div class="abs body" style="left:93px;top:88px;width:62px;text-align:center"><p class="pname">Project name</p>Lorem ipsum dolor sit amet, nec an dictas equidem appellantur, ut has commune accommodare. Mea illum, ludus solet idpro.</div>
  <div class="abs body" style="left:166px;top:88px;width:62px;text-align:center"><p class="pname">Project name</p>Lorem ipsum dolor sit amet, nec an dictas equidem appellantur, ut has commune accommodare. Mea illum, ludus solet idpro.</div>
  <div class="footer"><span class="fname"><i></i>Corvath</span><div class="bar">CORVATH | Copyright ©</div><div class="num">14</div></div>
</section>

<!-- 15 -->
<section class="slide">
  <div class="abs" role="img" aria-label="Monochrome image of DNA double helix strands" style="left:0;top:0;width:189px;height:95px;background:linear-gradient(135deg,#2a2a2a,#8c8c8c 45%,#3a3a3a)"></div>
  <div class="abs" style="left:123px;top:41px;width:98px;height:63px;border-radius:6px;background:linear-gradient(135deg,var(--magenta),var(--plum));color:#fff;display:flex;align-items:center;justify-content:center;text-align:center;font-size:9px;line-height:11px;font-weight:600">Here is a place<br>for short<br>statement</div>
  <h2 class="abs" style="left:0;right:0;top:107px;text-align:center;font-size:13px;font-weight:600">Heading + Text + Image Slide</h2>
  <div class="footer"><span class="fname"><i></i>Corvath</span><div class="bar">CORVATH | Copyright ©</div><div class="num">15</div></div>
</section>

<!-- 16 -->
<section class="slide">
  <h2 class="title center" style="top:16px">3 Columns Slide</h2>
  <div class="card" style="left:35px;background:var(--orange)"><div class="icon-ring"></div><p class="pname">Project name here</p><p class="body">Lorem ipsum dolor sit amet, nec an dictas equidem appellantur, ut has commune accommodare. Mea illum, ludus solet idpro.</p></div>
  <div class="card" style="left:99px;background:var(--magenta)"><div class="icon-ring"></div><p class="pname">Project name here</p><p class="body">Lorem ipsum dolor sit amet, nec an dictas equidem appellantur, ut has commune accommodare. Mea illum, ludus solet idpro.</p></div>
  <div class="card" style="left:163px;background:var(--plum)"><div class="icon-ring"></div><p class="pname">Project name here</p><p class="body">Lorem ipsum dolor sit amet, nec an dictas equidem appellantur, ut has commune accommodare. Mea illum, ludus solet idpro.</p></div>
  <div class="footer"><span class="fname"><i></i>Corvath</span><div class="bar">CORVATH | Copyright ©</div><div class="num">16</div></div>
</section>

<!-- 17 -->
<section class="slide">
  <h2 class="title center" style="top:13px">Table Slide</h2>
  <table class="data abs" style="left:23px;top:42px">
    <tr><th>Text</th><th>Text</th><th>Text</th><th>Text</th><th>Text</th></tr>
    <tr><td class="key">Data</td><td>Data</td><td>Data</td><td>Data</td><td>Data</td></tr>
    <tr><td class="key">Data</td><td>Data</td><td>Data</td><td>Data</td><td>Data</td></tr>
    <tr><td class="key">Data</td><td>Data</td><td>Data</td><td>Data</td><td>Data</td></tr>
    <tr><td class="key">Data</td><td>Data</td><td>Data</td><td>Data</td><td>Data</td></tr>
    <tr><td class="key">Data</td><td>Data</td><td>Data</td><td>Data</td><td>Data</td></tr>
    <tr><td class="key">Data</td><td>Data</td><td>Data</td><td>Data</td><td>Data</td></tr>
  </table>
  <div class="footer"><span class="fname"><i></i>Corvath</span><div class="bar">CORVATH | Copyright ©</div><div class="num">17</div></div>
</section>

<!-- 18 -->
<section class="slide">
  <h2 class="title" style="left:22px;top:13px">Smart Art Slide</h2>
  <div class="item" style="left:22px;top:41px;width:100px"><div class="icon-ring"></div><div><p class="pname">Project name</p><p class="body">Lorem ipsum dolor sit amet, nec an dictas equidem appellantur, ut has commune accommodare. Mea illum, ludus solet idpro.</p></div></div>
  <div class="item" style="left:22px;top:69px;width:100px"><div class="icon-ring"></div><div><p class="pname">Project name</p><p class="body">Lorem ipsum dolor sit amet, nec an dictas equidem appellantur, ut has commune accommodare. Mea illum, ludus solet idpro.</p></div></div>
  <div class="item" style="left:22px;top:96px;width:100px"><div class="icon-ring"></div><div><p class="pname">Project name</p><p class="body">Lorem ipsum dolor sit amet, nec an dictas equidem appellantur, ut has commune accommodare. Mea illum, ludus solet idpro.</p></div></div>
  <svg class="abs" style="left:0;top:0" width="252" height="142" aria-hidden="true">
    <path d="M189 24 L211 62 L200 73 H178 L167 62 Z" fill="var(--orange)"/>
    <path d="M175 77 H196 L196 115 H135 Z" fill="var(--magenta)" stroke-linejoin="round"/>
    <path d="M203 77 L240 115 H202 Z" fill="var(--plum)"/>
    <path d="M196 115 V77 H203" fill="none"/>
  </svg>
  <div class="abs body" style="left:170px;top:38px;width:38px;text-align:center;color:#fff"><p class="pname" style="color:#fff">Project<br>name</p>Lorem ipsum dolor sit amet, nec an dictas</div>
  <div class="abs body" style="left:160px;top:90px;width:36px;text-align:center;color:#fff"><p class="pname" style="color:#fff">Project name</p>Lorem ipsum dolor sit amet</div>
  <div class="abs body" style="left:202px;top:90px;width:34px;text-align:center;color:#fff"><p class="pname" style="color:#fff">Project name</p>Lorem ipsum dolor sit</div>
  <div class="footer"><span class="fname"><i></i>Corvath</span><div class="bar">CORVATH | Copyright ©</div><div class="num">18</div></div>
</section>

<!-- 19 -->
<section class="slide">
  <h2 class="title center" style="top:12px">Infographic</h2>
  <svg class="abs" style="left:0;top:0" width="252" height="142" aria-hidden="true">
    <g stroke-width="16" fill="none">
      <path d="M126 87 m0 -32 a32 32 0 0 1 32 32" stroke="var(--magenta)"/>
      <path d="M158 87 a32 32 0 0 1 -32 32" stroke="var(--orange)"/>
      <path d="M126 119 a32 32 0 0 1 -32 -32" stroke="var(--plum)"/>
      <path d="M94 87 a32 32 0 0 1 32 -32" stroke="var(--orange)"/>
    </g>
    <g stroke="#fff" stroke-width="1.2"><line x1="126" y1="47" x2="126" y2="63"/><line x1="126" y1="111" x2="126" y2="127"/><line x1="86" y1="87" x2="102" y2="87"/><line x1="150" y1="87" x2="166" y2="87"/></g>
    <circle cx="126" cy="87" r="21" fill="#fff"/>
  </svg>
  <div class="abs" style="left:110px;top:83px;font-size:5px;font-weight:600;color:var(--plum);display:flex;align-items:center;gap:1.5px"><i style="display:block;width:5px;height:5px;background:var(--plum)"></i>Corvath</div>
  <div class="abs body" style="left:14px;top:44px;width:72px;text-align:right"><p class="pname">Project name</p>Lorem ipsum dolor sit amet, nec an dictas equidem appellantur, ut has commune accommodare. Mea illum, ludus solet idpro.</div>
  <div class="abs body" style="left:14px;top:94px;width:72px;text-align:right"><p class="pname">Project name</p>Lorem ipsum dolor sit amet, nec an dictas equidem appellantur, ut has commune accommodare. Mea illum, ludus solet idpro.</div>
  <div class="abs body" style="left:168px;top:43px;width:72px"><p class="pname">Project name</p>Lorem ipsum dolor sit amet, nec an dictas equidem appellantur, ut has commune accommodare. Mea illum, ludus solet idpro.</div>
  <div class="abs body" style="left:168px;top:93px;width:72px"><p class="pname">Project name</p>Lorem ipsum dolor sit amet, nec an dictas equidem appellantur, ut has commune accommodare. Mea illum, ludus solet idpro.</div>
  <div class="footer"><span class="fname"><i></i>Corvath</span><div class="bar">CORVATH | Copyright ©</div><div class="num">19</div></div>
</section>

<!-- 20 -->
<section class="slide">
  <h2 class="title center" style="top:12px">Here Add Your Title</h2>
  <p class="abs body" style="left:44px;top:38px;width:164px;text-align:center;color:var(--plum)">Lorem Ipsum the printing and typesetting industry. Lorem Ipsum has been the industry's standard dummy text ever since the 1500s, when an unknown printer took a galley of type and scrambled it to make a type specimen book. It has survived not only five centuries.</p>
  <svg class="abs" style="left:0;top:0" width="252" height="142" aria-hidden="true">
    <g fill="none" stroke-width="2.6">
      <circle cx="74" cy="84" r="17" stroke="#eee"/><circle cx="74" cy="84" r="17" stroke="var(--orange)" stroke-dasharray="53.4 106.8" transform="rotate(-90 74 84)"/>
      <circle cx="126" cy="84" r="17" stroke="#eee"/><circle cx="126" cy="84" r="17" stroke="var(--orange)" stroke-dasharray="80.1 106.8" transform="rotate(-90 126 84)"/>
      <circle cx="178" cy="84" r="17" stroke="#eee"/><circle cx="178" cy="84" r="17" stroke="var(--orange)" stroke-dasharray="42.7 106.8" transform="rotate(-90 178 84)"/>
    </g>
    <g font-family="Poppins, sans-serif" font-size="10" font-weight="600" fill="var(--plum)" text-anchor="middle">
      <text x="74" y="88">50%</text><text x="126" y="88">75%</text><text x="178" y="88">40%</text>
    </g>
  </svg>
  <p class="abs body" style="left:48px;top:108px;width:52px;text-align:center;color:var(--plum)">Lorem ipsum dolor amet amet consectetur dolor</p>
  <p class="abs body" style="left:100px;top:108px;width:52px;text-align:center;color:var(--plum)">Lorem ipsum dolor amet amet consectetur dolor</p>
  <p class="abs body" style="left:152px;top:108px;width:52px;text-align:center;color:var(--plum)">Lorem ipsum dolor amet amet consectetur dolor</p>
  <div class="footer"><span class="fname"><i></i>Corvath</span><div class="bar">CORVATH | Copyright ©</div><div class="num">20</div></div>
</section>

<!-- 21 -->
<section class="slide">
  <h2 class="title center" style="top:17px">Company Timeline</h2>
  <svg class="abs" style="left:0;top:0" width="252" height="142" aria-hidden="true">
    <g>
      <path d="M21 54 H62 L69 66 L62 78 H21 L27 66 Z" fill="var(--plum)"/>
      <path d="M62 54 H103 L110 66 L103 78 H62 L69 66 Z" fill="var(--orange)"/>
      <path d="M103 54 H144 L151 66 L144 78 H103 L110 66 Z" fill="var(--plum)"/>
      <path d="M144 54 H185 L192 66 L185 78 H144 L151 66 Z" fill="var(--orange)"/>
      <path d="M185 54 H226 L233 66 L226 78 H185 L192 66 Z" fill="var(--plum)"/>
    </g>
    <g stroke="#fff" stroke-width="1.2" fill="none"><path d="M62 54 L69 66 L62 78"/><path d="M103 54 L110 66 L103 78"/><path d="M144 54 L151 66 L144 78"/><path d="M185 54 L192 66 L185 78"/></g>
    <g font-family="Poppins, sans-serif" font-size="4.4" font-weight="600" fill="#fff" text-anchor="middle">
      <text x="47" y="67.5">STEP 01</text><text x="88" y="67.5">STEP 02</text><text x="129" y="67.5">STEP 03</text><text x="170" y="67.5">STEP 04</text><text x="211" y="67.5">STEP 05</text>
    </g>
  </svg>
  <div class="abs body" style="left:24px;top:88px;width:38px;text-align:center"><p class="pname" style="color:var(--ink)">Project name</p>Lorem Ipsum is simply dummy unknown printer took a galley of type and scrambled it.</div>
  <div class="abs body" style="left:66px;top:88px;width:38px;text-align:center"><p class="pname" style="color:var(--ink)">Project name</p>Lorem Ipsum is simply dummy unknown printer took a galley of type and scrambled it.</div>
  <div class="abs body" style="left:108px;top:88px;width:38px;text-align:center"><p class="pname" style="color:var(--ink)">Project name</p>Lorem Ipsum is simply dummy unknown printer took a galley of type and scrambled it.</div>
  <div class="abs body" style="left:150px;top:88px;width:38px;text-align:center"><p class="pname" style="color:var(--ink)">Project name</p>Lorem Ipsum is simply dummy unknown printer took a galley of type and scrambled it.</div>
  <div class="abs body" style="left:190px;top:88px;width:38px;text-align:center"><p class="pname" style="color:var(--ink)">Project name</p>Lorem Ipsum is simply dummy unknown printer took a galley of type and scrambled it.</div>
  <div class="footer"><span class="fname"><i></i>Corvath</span><div class="bar">CORVATH | Copyright ©</div><div class="num">21</div></div>
</section>

<!-- 22 -->
<section class="slide" style="background:linear-gradient(160deg,#fff,#f2f2f4)">
  <div class="abs" style="left:47px;top:19px;font-size:8px;font-weight:600;color:var(--magenta);display:flex;align-items:center;gap:3px"><i style="display:block;width:9px;height:9px;background:var(--magenta)"></i>Corvath Therapeutics</div>
  <div class="contact top" style="top:37px"><svg width="5" height="5" viewBox="0 0 10 10"><circle cx="5" cy="5" r="4" fill="none" stroke="#fff"/><path d="M1 5H9M5 1C3 3.5 3 6.5 5 9M5 1C7 3.5 7 6.5 5 9" stroke="#fff" fill="none" stroke-width=".8"/></svg>www.website.com</div>
  <div class="contact" style="top:55px"><svg width="5" height="6" viewBox="0 0 10 12"><path d="M5 12C5 12 1 7 1 4.5A4 4 0 0 1 9 4.5C9 7 5 12 5 12Z" fill="var(--orange)"/><circle cx="5" cy="4.5" r="1.5" fill="#fff"/></svg>Here to write your<br>Company adress</div>
  <div class="contact" style="top:73px"><svg width="5" height="5" viewBox="0 0 10 10"><path d="M2 1L4 3L3 4.5C4 6.5 5 7 5.5 7L7 6L9 8L7.5 9.5C4 9.5 .5 6 .5 2.5Z" fill="var(--orange)"/></svg>(555) 014 2290</div>
  <div class="contact" style="top:91px"><svg width="6" height="4" viewBox="0 0 12 8"><rect width="12" height="8" fill="var(--orange)"/><path d="M0 0L6 5L12 0" stroke="#fff" fill="none"/></svg>info@website.com</div>
  <div class="abs" style="left:57px;top:111px;display:flex;gap:2px"><i style="width:4.5px;height:4.5px;background:var(--ink)"></i><i style="width:4.5px;height:4.5px;background:var(--ink)"></i><i style="width:4.5px;height:4.5px;background:var(--ink)"></i><i style="width:4.5px;height:4.5px;background:var(--ink)"></i></div>
  <h2 class="abs" style="left:144px;top:63px;font-size:14px;font-weight:600;color:var(--plum)">Thank You</h2>
</section>

</main>
</body>
</html>
```